Verostel business card

Business card for sustainable investment company called "Verostel". Verostel is an exchange platform selling carbon credits between buyers and sellers. Carbon Credits are an environmental commodity for reducing global carbon emissions.

the card should obviously have our logo and the theme should be sustainability/environment mixed with a trading platform.

Contact Information for Business Card

Logo, Name, Title, Phone, Email

Colors
0054AA
0677BA
7BADD7
CADEEF
E8F1F8
0094D4
00A9DD
6FCCEA
C7EBF8
E9F6FB
00AB8E
00BBA5
67D7C9
C6EFE9
E9F9F6
59FF00
82FF00
B8FF75
E3FFCB
F4FFEA

```html
<!DOCTYPE html>
<html lang="en">
<head>
<meta charset="utf-8">
<title>Verostel Business Card</title>
<link href="https://fonts.googleapis.com/css2?family=Montserrat:wght@500;600&family=Inter:wght@400&display=swap" rel="stylesheet">
<style>
  :root {
    --backdrop: #8f8f8f;
    --card: #f1f1f1;
    --navy: #0d2a4f;
    --brand-blue: #1ea7f0;
    --title-grey: #8c8c8c;
    --contact-grey: #6f6f6f;
  }
  * { margin: 0; padding: 0; box-sizing: border-box; }
  html, body {
    width: 1200px;
    height: 1000px;
    overflow: hidden;
    background: var(--backdrop);
  }
  .canvas {
    width: 1200px;
    height: 1000px;
    display: flex;
    align-items: center;
    justify-content: center;
  }
  .business-card {
    width: 840px;
    height: 480px;
    background: var(--card);
    display: flex;
    flex-direction: column;
    align-items: center;
    justify-content: center;
    text-align: center;
  }
  .brand-mark {
    width: 112px;
    height: 112px;
    border-radius: 50%;
    background: var(--brand-blue);
    margin-bottom: 22px;
  }
  .brand-name {
    font-family: "Montserrat", sans-serif;
    font-weight: 600;
    font-size: 58px;
    line-height: 1;
    color: var(--navy);
    letter-spacing: 0.01em;
    margin-bottom: 26px;
  }
  .person-name {
    font-family: "Montserrat", sans-serif;
    font-weight: 600;
    font-size: 27px;
    color: var(--navy);
    line-height: 1.1;
  }
  .person-title {
    font-family: "Inter", sans-serif;
    font-weight: 400;
    font-size: 23px;
    color: var(--title-grey);
    margin-top: 4px;
    margin-bottom: 14px;
  }
  .contact-line {
    font-family: "Inter", sans-serif;
    font-weight: 400;
    font-size: 21px;
    letter-spacing: 0.18em;
    color: var(--contact-grey);
    line-height: 1.5;
    text-transform: uppercase;
  }
</style>
</head>
<body>
  <main class="canvas">
    <section class="business-card" aria-label="Verostel business card">
      <div class="brand-mark" aria-hidden="true"></div>
      <h1 class="brand-name">VEROSTEL</h1>
      <p class="person-name">Name Surname</p>
      <p class="person-title">Title</p>
      <p class="contact-line">name@verostel.com • 012•345•6789</p>
      <p class="contact-line">verostel.com</p>
    </section>
  </main>
</body>
</html>
```